Business Card Design Project

Need a business card with logo that is attached.
Company name: Tolmen Brisk Solutions, LLC
My name: Lorna Tolmen
Title: President
Phone number: 703-555-0148
Email: ltolmen@tolmenbrisksolutions.example
web site: www.tolmenbrisksolutions.example

Industry/Entity Type

Business

```html
<!DOCTYPE html>
<html lang="en">
<head>
<meta charset="utf-8">
<title>Tolmen Brisk Solutions, LLC – Business Card</title>
<link rel="stylesheet" href="https://fonts.googleapis.com/css2?family=Tinos&family=Questrial&display=swap">
<style>
  :root {
    --card-charcoal: #4d4a47;
    --band-blue: #0a7cc4;
    --paper-white: #ffffff;
    --ink-black: #1a1a1a;
    --title-grey: #3d3a3a;
    --serif: "Tinos", "Times New Roman", serif;
    --sans: "Questrial", "Century Gothic", sans-serif;
  }
  html, body {
    margin: 0;
    padding: 0;
    width: 1200px;
    height: 686px;
    overflow: hidden;
    background: var(--paper-white);
  }
  .card {
    position: relative;
    width: 1200px;
    height: 686px;
    background: var(--card-charcoal);
    border-radius: 34px;
    overflow: hidden;
  }
  .blue-band {
    position: absolute;
    left: 0;
    top: 130px;
    width: 1200px;
    height: 411px;
    background: var(--band-blue);
  }
  .logo-frame {
    position: absolute;
    left: 40px;
    top: 184px;
    width: 312px;
    height: 303px;
    background: var(--paper-white);
  }
  .logo-tile {
    position: absolute;
    left: 32px;
    top: 34px;
    width: 249px;
    height: 232px;
    background: var(--card-charcoal);
    display: flex;
    align-items: center;
    justify-content: center;
    text-align: center;
  }
  .logo-name {
    font-family: var(--serif);
    font-size: 30px;
    line-height: 1.15;
    color: var(--paper-white);
    margin: 0;
  }
  .company-name {
    position: absolute;
    left: 371px;
    top: 254px;
    margin: 0;
    font-family: var(--serif);
    font-weight: 400;
    font-size: 46px;
    line-height: 57px;
    color: var(--paper-white);
    letter-spacing: 0.5px;
  }
  .person {
    position: absolute;
    right: 40px;
    top: 176px;
    text-align: right;
  }
  .person-name {
    margin: 0;
    font-family: var(--sans);
    font-size: 44px;
    line-height: 50px;
    color: var(--ink-black);
    letter-spacing: -1px;
  }
  .person-title {
    margin: 2px 0 0;
    font-family: var(--serif);
    font-size: 23px;
    letter-spacing: 8px;
    color: var(--title-grey);
    margin-right: -6px;
  }
  .contact {
    position: absolute;
    right: 40px;
    top: 396px;
    margin: 0;
    text-align: right;
    font-family: var(--sans);
    font-style: normal;
    font-size: 22px;
    line-height: 31px;
    color: var(--paper-white);
  }
  .contact-line { display: block; }
</style>
</head>
<body>
  <div class="card">
    <div class="blue-band"></div>

    <div class="logo-frame">
      <div class="logo-tile">
        <p class="logo-name">Tolmen Brisk<br>Solutions</p>
      </div>
    </div>

    <h1 class="company-name">TOLMEN BRISK<br>SOLUTIONS<br>LLC</h1>

    <div class="person">
      <p class="person-name">LORNA TOLMEN</p>
      <p class="person-title">PRESIDENT</p>
    </div>

    <address class="contact">
      <span class="contact-line">703-555-0148</span>
      <span class="contact-line">ltolmen@tolmenbrisksolutions.example</span>
      <span class="contact-line">www.tolmenbrisksolutions.example</span>
    </address>
  </div>
</body>
</html>
```